Banners for website home page

I'm looking for 3 banners that will rotate on my website carousel addressing my 3 target markets. The website is Ledgerwise Harbor.

1) Young Starters
Headline: Start smart. Invest with confidence.
Sub: Learn the basics, set your first goal, and build a long-term plan with Ledgerwise Harbor.
CTA: Start free
Hero image ideas: Young person with phone/laptop; app UI overlay; subtle navy/gold chart shapes.

2) Saving for a Goal
Headline: Turn your goal into a plan.
Sub: Home deposit or child’s education—set targets, see projections, and track progress.
CTA: Plan my goal
Hero image ideas: Couple/family looking at house plans or a uni cap; progress bar overlay; warm light.

3) Retirement Fund Owners
Headline: Grow and protect your Retirement Fund.
Sub: Professional-grade tracking and signals to help your super grow—and last.
CTA: Start Now
Hero image ideas: Mature couple with tablet / beach walk; portfolio charts/compass motif overlaid.

Our app does the following:
Ledgerwise Harbor is an easy-to-use app designed to help everyday people take control of their investing journey.
Backed by over 10 years of proven investment models and experience, it empowers you to set realistic goals, build a tailored investment plan, and confidently manage your risk. With built-in education, alerts, and market insights, Ledgerwise Harbor helps you stay on course and maximise returns—no guesswork, just smart investing.

See attached an example AI generated banner and current logo to base colours, feel. for the website I use a dark blue menu and below would like a lighter colour - yellow/gold/white banner background.

Banner sizes : 1600 x 700 and 1200x525
Square size for mobile : 960x960 and 640x640
Format: WebP and PNG

```html
<!DOCTYPE html>
<html lang="en">
<head>
<meta charset="utf-8">
<title>Ledgerwise Harbor – Young Starters Banner</title>
<link href="https://fonts.googleapis.com/css2?family=Poppins:wght@400;700&display=swap" rel="stylesheet">
<style>
  :root {
    --stage: #a7a8ab;
    --navy: #141b42;
    --gold: #c08a25;
    --cream: #f5e6c0;
    --white: #ffffff;
    --ink: #2b2b2b;
    --photo-top: #8a8480;
    --photo-bottom: #c9b896;
  }
  html, body {
    margin: 0;
    width: 1200px;
    height: 720px;
    overflow: hidden;
    background: var(--stage);
    font-family: "Poppins", sans-serif;
  }
  .banner {
    position: absolute;
    left: 90px;
    top: 138px;
    width: 1035px;
    height: 467px;
    background: var(--cream);
    overflow: hidden;
    box-shadow: 0 4px 14px rgba(0,0,0,0.25);
  }
  .banner-shapes {
    position: absolute;
    inset: 0;
    width: 100%;
    height: 100%;
  }
  .hero-photo {
    position: absolute;
    left: 249px;
    top: 32px;
    width: 275px;
    height: 435px;
    background: linear-gradient(180deg, var(--photo-top), var(--photo-bottom));
  }
  .brand {
    position: absolute;
    left: 40px;
    top: 34px;
    width: 160px;
    text-align: center;
    color: var(--white);
  }
  .brand-dot {
    display: block;
    width: 44px;
    height: 44px;
    margin: 0 auto 12px;
    border-radius: 50%;
    background: var(--gold);
  }
  .brand-name {
    margin: 0;
    font-weight: 400;
    font-size: 19px;
    line-height: 25px;
    letter-spacing: 2px;
    text-transform: uppercase;
  }
  .headline {
    position: absolute;
    left: 546px;
    top: 128px;
    margin: 0;
    font-weight: 700;
    font-size: 47px;
    line-height: 52px;
    color: var(--gold);
  }
  .subline {
    position: absolute;
    left: 546px;
    top: 288px;
    width: 365px;
    margin: 0;
    font-weight: 400;
    font-size: 21px;
    line-height: 32.5px;
    color: var(--white);
  }
  .cta {
    position: absolute;
    left: 543px;
    top: 409px;
    width: 145px;
    height: 35px;
    border-radius: 18px;
    background: var(--gold);
    color: var(--ink);
    font-weight: 700;
    font-size: 23px;
    line-height: 36px;
    text-align: center;
    text-decoration: none;
  }
</style>
</head>
<body>
  <section class="banner">
    <svg class="banner-shapes" viewBox="0 0 1595 720" preserveAspectRatio="none" aria-hidden="true">
      <polygon class="corner-navy" points="0,0 750,0 0,412" fill="var(--navy)"/>
      <path class="corner-gold-bottom" d="M0,557 Q40,695 240,720 L0,720 Z" fill="var(--gold)"/>
      <path class="corner-gold-top" d="M1432,0 Q1555,30 1595,112 L1595,0 Z" fill="var(--gold)"/>
      <path class="content-blob" d="M640,720 C700,450 850,80 1045,80 C1200,80 1300,200 1400,300 C1500,390 1540,470 1540,580 C1540,650 1480,700 1440,720 Z" fill="var(--navy)"/>
      <path class="blob-outline" d="M432,620 C420,520 700,42 1045,42 C1230,42 1330,180 1430,280 C1540,380 1578,470 1578,570 C1578,640 1530,690 1482,727" fill="none" stroke="var(--gold)" stroke-width="11"/>
      <circle class="dot-gold" cx="1482" cy="85" r="26" fill="var(--gold)"/>
      <circle class="dot-navy" cx="1457" cy="197" r="45" fill="var(--navy)"/>
      <circle class="dot-gold" cx="289" cy="509" r="26" fill="var(--gold)"/>
      <circle class="dot-navy" cx="262" cy="622" r="45" fill="var(--navy)"/>
    </svg>

    <div class="hero-photo" role="img" aria-label="Photo of a young man in a grey blazer looking at his phone while holding a laptop"></div>

    <div class="brand">
      <span class="brand-dot"></span>
      <p class="brand-name">Ledgerwise<br>Harbor</p>
    </div>

    <h1 class="headline">Start smart.<br>Invest with<br>confidence.</h1>
    <p class="subline">Learn the basics, set your first goal, and build a long-term plan with Ledgerwise Harbor.</p>
    <a class="cta" href="#">Start Free</a>
  </section>
</body>
</html>
```